Commercial Business Card - stand out, clean, simple, unique.

commercial real estate group located in Texas. Called 4 Ridges Real Estate. We want a unique yet clean and professional card. On one side I would like the 4R to be by itself or to look as unique or tasteful as possible. We have the logo in white, black, and color in case a black background or something similar looks best on one side. We need a space for our name, email, cell. website. And possibly room for a phrase or city.

Contact Information for Business Card

Name, Title, Email, Phone Number, website

```html
<!DOCTYPE html>
<html lang="en">
<head>
<meta charset="utf-8">
<title>4 Ridges Real Estate – Business Card</title>
<link rel="stylesheet" href="https://fonts.googleapis.com/css2?family=Open+Sans:wght@400;600;700&display=swap">
<style>
  :root {
    --navy: #14296b;
    --navy-deep: #0e1f55;
    --royal: #1f3f9a;
    --orange: #d9692a;
    --ink: #3b3b3b;
    --paper: #ffffff;
    --backdrop: #3a3a3d;
  }
  * { margin: 0; padding: 0; box-sizing: border-box; }
  html, body { width: 1200px; height: 1000px; overflow: hidden; }
  body {
    background: var(--backdrop);
    font-family: "Open Sans", Arial, sans-serif;
    position: relative;
  }
  .card {
    position: absolute;
    left: 250px;
    width: 700px;
    height: 400px;
    overflow: hidden;
  }
  /* Back side */
  .card-back {
    top: 60px;
    background: radial-gradient(ellipse at 55% 40%, #2348a8 0%, var(--royal) 35%, var(--navy-deep) 100%);
  }
  .card-back .brand-placeholder {
    position: absolute;
    left: 0; right: 0; top: 135px;
    text-align: center;
    font-weight: 700;
    font-size: 96px;
    line-height: 1;
    color: var(--paper);
  }
  .card-back .tagline {
    position: absolute;
    right: 60px; bottom: 40px;
    font-size: 20px;
    color: var(--paper);
  }
  /* Front side */
  .card-front {
    top: 540px;
    background: linear-gradient(160deg, #ffffff 0%, #f3f3f3 100%);
  }
  .brand {
    position: absolute;
    left: 48px; top: 118px;
    display: flex;
    align-items: center;
    gap: 12px;
  }
  .brand-square {
    width: 18px; height: 18px;
    background: var(--navy);
  }
  .brand-name {
    font-weight: 700;
    font-size: 24px;
    line-height: 1.15;
    color: var(--navy);
  }
  .contact {
    position: absolute;
    left: 410px; top: 118px;
    color: var(--ink);
    font-size: 17px;
    line-height: 1.3;
  }
  .contact .person {
    font-weight: 700;
    font-size: 22px;
    color: var(--navy);
  }
  .contact .title {
    font-size: 17px;
    color: var(--orange);
    margin-bottom: 4px;
  }
  .band {
    position: absolute;
    left: 0; right: 0; top: 300px;
    height: 46px;
    display: flex;
    align-items: center;
  }
  .band-web {
    flex: 0 0 78%;
    height: 100%;
    background: linear-gradient(90deg, var(--royal), var(--navy));
    color: var(--paper);
    font-size: 20px;
    letter-spacing: 7px;
    display: flex;
    align-items: center;
    padding-left: 190px;
  }
  .band-brand {
    flex: 0 0 10%;
    text-align: center;
    font-weight: 700;
    font-size: 24px;
    color: var(--navy);
  }
  .band-accent {
    flex: 1;
    height: 100%;
    background: var(--orange);
  }
</style>
</head>
<body>
  <section class="card card-back" aria-label="Card back">
    <div class="brand-placeholder">4R</div>
    <p class="tagline">find your ideal home</p>
  </section>

  <section class="card card-front" aria-label="Card front">
    <div class="brand">
      <div class="brand-square"></div>
      <div class="brand-name">4 Ridges<br>Real Estate</div>
    </div>

    <div class="contact">
      <div class="person">DANIEL MARSH</div>
      <div class="title">PRESIDENT</div>
      <div>P: 512 4406 1837</div>
      <div>M: 512 9183 2764</div>
      <div>daniel@4ridges.com</div>
    </div>

    <div class="band">
      <div class="band-web">www.4ridges.com</div>
      <div class="band-brand">4R</div>
      <div class="band-accent"></div>
    </div>
  </section>
</body>
</html>
```